Convert lettering into a cool graphic

We exchange old heating boilers for new boilers or heat pumps. In addition, I would like a graphic with the lettering "The wandering heron" in a rusty, old, or burned-in look.
The metal background can also be a piece of metal with lettering. Attached is a draft of what this might look like. In addition, I send the logo from us so that you can see the current lettering. It doesn't have to look the same, the graphics just have to match the logo.

```html
<!DOCTYPE html>
<html lang="en">
<head>
<meta charset="utf-8">
<title>The Wandering Heron – Halvern Service GmbH</title>
<link rel="stylesheet" href="https://fonts.googleapis.com/css2?family=Barlow+Condensed:wght@700&family=Michroma&display=swap">
<style>
  :root {
    --fog-top: #dcdcdc;
    --fog-mid: #8c8f99;
    --glass-dark: #2a2a3a;
    --glass-deep: #1c1c28;
    --logo-ink: #2b2a30;
    --steel: #e4e1dc;
  }
  html, body {
    margin: 0;
    padding: 0;
    width: 1200px;
    height: 866px;
    overflow: hidden;
    background: var(--glass-deep);
  }
  .canvas {
    position: relative;
    width: 1200px;
    height: 866px;
    overflow: hidden;
  }
  .backdrop {
    position: absolute;
    inset: 0;
    background:
      radial-gradient(ellipse at 50% 20%, rgba(255,255,255,0.25), transparent 60%),
      linear-gradient(to bottom, var(--fog-top) 0%, #c7c8cc 14%, var(--fog-mid) 30%, var(--glass-dark) 48%, var(--glass-deep) 100%);
  }
  .brand {
    position: absolute;
    left: 269px;
    top: 204px;
    display: flex;
    align-items: center;
    gap: 27px;
    color: var(--logo-ink);
    font-family: "Michroma", sans-serif;
    opacity: 0.85;
  }
  .brand-square {
    width: 154px;
    height: 129px;
    background: var(--logo-ink);
    border-radius: 14px;
  }
  .brand-name {
    display: flex;
    flex-direction: column;
    gap: 8px;
    padding-top: 14px;
  }
  .brand-title {
    font-size: 60px;
    line-height: 1;
    letter-spacing: 8px;
  }
  .brand-sub {
    font-size: 21px;
    line-height: 1;
    letter-spacing: 5px;
  }
  .plate {
    position: absolute;
    left: 238px;
    top: 402px;
    width: 751px;
    height: 159px;
  }
  .plate svg {
    position: absolute;
    inset: 0;
  }
  .plate-label {
    font-family: "Barlow Condensed", sans-serif;
    font-weight: 700;
    font-size: 68px;
    letter-spacing: 4px;
    fill: var(--steel);
  }
</style>
</head>
<body>
<div class="canvas">
  <div class="backdrop" role="img" aria-label="Fogged glass pane with condensation droplets, fading from pale grey mist to dark navy"></div>

  <div class="brand">
    <div class="brand-square"></div>
    <div class="brand-name">
      <span class="brand-title">HALVERN</span>
      <span class="brand-sub">SERVICE GMBH</span>
    </div>
  </div>

  <div class="plate">
    <svg width="751" height="159" viewBox="0 0 751 159">
      <defs>
        <linearGradient id="rust-frame" x1="0" y1="0" x2="0" y2="1">
          <stop offset="0" stop-color="#8a4a2c"/>
          <stop offset="0.5" stop-color="#5e2c16"/>
          <stop offset="1" stop-color="#7a4228"/>
        </linearGradient>
        <linearGradient id="rust-recess" x1="0" y1="0" x2="0" y2="1">
          <stop offset="0" stop-color="#3e1c0e"/>
          <stop offset="0.45" stop-color="#6e3218"/>
          <stop offset="1" stop-color="#4e2412"/>
        </linearGradient>

        <filter id="rust-mottle" x="0" y="0" width="100%" height="100%">
          <feTurbulence type="fractalNoise" baseFrequency="0.04 0.09" numOctaves="3" seed="7" result="noise"/>
          <feColorMatrix in="noise" type="matrix"
            values="0 0 0 0 0.62  0 0 0 0 0.26  0 0 0 0 0.10  3 0 0 0 -1.3" result="patch"/>
          <feComposite in="patch" in2="SourceGraphic" operator="in"/>
        </filter>

        <filter id="rust-pits" x="0" y="0" width="100%" height="100%">
          <feTurbulence type="fractalNoise" baseFrequency="0.7" numOctaves="3" seed="11" result="noise"/>
          <feColorMatrix in="noise" type="matrix"
            values="0 0 0 0 0.16  0 0 0 0 0.07  0 0 0 0 0.03  10 0 0 0 -5.6" result="pits"/>
          <feComposite in="pits" in2="SourceGraphic" operator="in"/>
        </filter>

        <filter id="scale-flecks" x="0" y="0" width="100%" height="100%">
          <feTurbulence type="fractalNoise" baseFrequency="0.85" numOctaves="2" seed="3" result="noise"/>
          <feColorMatrix in="noise" type="matrix"
            values="0 0 0 0 0.78  0 0 0 0 0.74  0 0 0 0 0.70  12 0 0 0 -7.4" result="flecks"/>
          <feComposite in="flecks" in2="SourceGraphic" operator="in"/>
        </filter>

        <filter id="worn-letters" x="-5%" y="-20%" width="110%" height="140%">
          <feTurbulence type="fractalNoise" baseFrequency="0.9" numOctaves="3" seed="5" result="noise"/>
          <feColorMatrix in="noise" type="matrix"
            values="0 0 0 0 0.45  0 0 0 0 0.24  0 0 0 0 0.14  10 0 0 0 -5.9" result="stain"/>
          <feComposite in="stain" in2="SourceGraphic" operator="in" result="stain-in"/>
          <feMerge result="letter">
            <feMergeNode in="SourceGraphic"/>
            <feMergeNode in="stain-in"/>
          </feMerge>
          <feOffset in="SourceAlpha" dx="2" dy="3" result="offset"/>
          <feGaussianBlur in="offset" stdDeviation="1.5" result="blur"/>
          <feColorMatrix in="blur" type="matrix"
            values="0 0 0 0 0.12  0 0 0 0 0.04  0 0 0 0 0.01  0 0 0 0.85 0" result="shadow"/>
          <feMerge>
            <feMergeNode in="shadow"/>
            <feMergeNode in="letter"/>
          </feMerge>
        </filter>

        <clipPath id="frame-shape">
          <rect x="2" y="2" width="747" height="155" rx="28"/>
        </clipPath>
        <clipPath id="recess-shape">
          <rect x="34" y="22" width="686" height="110" rx="12"/>
        </clipPath>
      </defs>

      <g class="plate-frame" clip-path="url(#frame-shape)">
        <rect x="2" y="2" width="747" height="155" rx="28" fill="url(#rust-frame)"/>
        <rect x="2" y="2" width="747" height="155" fill="#fff" filter="url(#rust-mottle)"/>
        <rect x="2" y="2" width="747" height="155" fill="#fff" filter="url(#rust-pits)"/>
        <rect x="2" y="2" width="747" height="155" fill="#fff" filter="url(#scale-flecks)"/>
      </g>
      <rect x="2" y="2" width="747" height="155" rx="28" fill="none" stroke="#2a1208" stroke-width="2"/>

      <g class="plate-recess" clip-path="url(#recess-shape)">
        <rect x="34" y="22" width="686" height="110" fill="url(#rust-recess)"/>
        <rect x="34" y="22" width="686" height="110" fill="#fff" filter="url(#rust-mottle)"/>
        <rect x="34" y="22" width="686" height="110" fill="#fff" filter="url(#rust-pits)" opacity="0.8"/>
        <rect x="34" y="22" width="686" height="110" fill="#fff" filter="url(#scale-flecks)" opacity="0.35"/>
        <rect x="34" y="22" width="686" height="110" rx="12" fill="none" stroke="#1e0c04" stroke-width="8" opacity="0.55"/>
      </g>
      <rect x="34" y="22" width="686" height="110" rx="12" fill="none" stroke="#a8826a" stroke-width="2" opacity="0.7"/>

      <text class="plate-label" x="376" y="106" text-anchor="middle" filter="url(#worn-letters)">THE WANDERING HERON</text>
    </svg>
  </div>
</div>
</body>
</html>
```